Yard Sign Design Needed

Yard sign needed for mowing & landscaping company. Would like to use the top logo with black background which is attached. Would like MOWING to be in large standout letters. The word "landscaping" can be smaller and more artistic or omitted. Will need room for phone number once design is approved. The phone number will need to stand out and look identical/similar to the word 'MOWING"

```html
<!DOCTYPE html>
<html lang="en">
<head>
<meta charset="utf-8">
<title>Brennick Contractors – Mowing Yard Sign</title>
<link rel="stylesheet" href="https://fonts.googleapis.com/css2?family=Archivo:wght@700;900&family=Kaushan+Script&display=swap">
<style>
  :root {
    --page-bg: #e9ebe6;
    --sign-black: #222222;
    --lime: #8dc021;
    --lime-bright: #9fd034;
    --olive: #7d8a08;
    --grass-light: #8fd04a;
    --grass-dark: #2f7d12;
    --white: #ffffff;
    --ink: #0b0b0b;
  }
  * { margin: 0; padding: 0; box-sizing: border-box; }
  html, body {
    width: 1200px; height: 1200px; overflow: hidden;
    background: var(--page-bg);
  }
  .yard-sign {
    position: absolute; left: 175px; top: 40px;
    width: 850px; height: 1120px;
    background: var(--white);
    overflow: hidden;
    box-shadow: 0 10px 30px rgba(0,0,0,0.18);
  }
  .sign-top {
    position: absolute; left: 0; top: 0; width: 850px; height: 640px;
    background: var(--sign-black);
  }
  .inner-frame {
    position: absolute; left: 30px; top: 30px; width: 790px; height: 560px;
    border: 4px solid var(--lime);
  }
  .brand {
    position: absolute; left: 0; top: 100px; width: 850px;
    text-align: center; font-family: "Archivo", Arial, sans-serif;
    font-weight: 700; color: var(--lime-bright); white-space: nowrap;
  }
  .brand-mark {
    display: block; width: 110px; height: 110px; margin: 0 auto 30px;
    background: var(--lime-bright);
  }
  .brand-name { font-size: 62px; letter-spacing: 10px; line-height: 1; }
  .brand-sub { font-size: 28px; letter-spacing: 8px; margin-top: 12px; }
  .service-script {
    position: absolute; left: 120px; top: 388px; width: 700px; text-align: center;
    font-family: "Kaushan Script", cursive; font-size: 60px; line-height: 1.2;
    color: var(--lime-bright); transform: rotate(4deg); white-space: nowrap;
  }
  .lawn-photo {
    position: absolute; left: 0; top: 500px; width: 850px; height: 420px;
    background: linear-gradient(160deg, var(--grass-light) 0%, #5eb02a 45%, var(--grass-dark) 100%);
  }
  .wave { position: absolute; left: 0; top: 440px; width: 850px; height: 260px; }
  .white-band {
    position: absolute; left: 0; top: 905px; width: 850px; height: 215px;
    background: var(--white);
  }
  .headline-box {
    position: absolute; left: 180px; top: 858px; width: 540px; height: 136px;
    background: var(--lime); border: 5px solid var(--white);
    box-shadow: 0 8px 12px rgba(0,0,0,0.35);
    display: flex; align-items: center; justify-content: center;
  }
  .headline {
    font-family: "Archivo", Arial, sans-serif; font-weight: 900;
    font-size: 96px; color: var(--ink); letter-spacing: -2px; line-height: 1;
    white-space: nowrap;
  }
  .phone-line {
    position: absolute; left: 0; top: 1008px; width: 850px;
    display: flex; align-items: center; justify-content: center; gap: 16px;
  }
  .phone-icon { width: 80px; height: 80px; flex: none; }
  .phone-number {
    font-family: "Archivo", Arial, sans-serif; font-weight: 900;
    font-size: 86px; color: var(--ink); letter-spacing: -2px; line-height: 1;
    white-space: nowrap;
  }
</style>
</head>
<body>
  <div class="yard-sign">
    <div class="sign-top">
      <div class="inner-frame"></div>
    </div>

    <div class="lawn-photo" role="img" aria-label="Photo of a freshly mowed green lawn with a red push mower on the right"></div>

    <svg class="wave" viewBox="0 0 850 260" preserveAspectRatio="none" aria-hidden="true">
      <path d="M0 0 H850 V240 C700 250 620 200 480 140 C330 75 180 50 0 75 Z" fill="var(--sign-black)"/>
      <path d="M0 70 C180 45 330 70 480 135 C620 195 700 245 850 232 V205 C700 225 620 175 480 115 C330 50 180 30 0 50 Z" fill="var(--olive)"/>
    </svg>

    <div class="brand">
      <span class="brand-mark"></span>
      <div class="brand-name">BRENNICK</div>
      <div class="brand-sub">CONTRACTORS LLC</div>
    </div>
    <div class="service-script">Landscaping</div>

    <div class="white-band"></div>

    <div class="headline-box"><span class="headline">MOWING</span></div>

    <div class="phone-line">
      <svg class="phone-icon" viewBox="0 0 100 100" aria-hidden="true">
        <path d="M22 20 C14 24 10 34 16 48 C26 70 44 84 62 90 C74 94 82 88 86 80 L74 66 C70 62 66 62 62 66 L58 70 C48 66 36 54 32 44 L36 40 C40 36 40 32 36 28 Z" fill="var(--lime)"/>
        <path d="M56 34 A12 12 0 0 1 68 46" stroke="var(--lime)" stroke-width="6" fill="none" stroke-linecap="round"/>
        <path d="M58 20 A26 26 0 0 1 82 44" stroke="var(--lime)" stroke-width="6" fill="none" stroke-linecap="round"/>
        <path d="M60 6 A40 40 0 0 1 96 42" stroke="var(--lime)" stroke-width="6" fill="none" stroke-linecap="round"/>
      </svg>
      <span class="phone-number">555.010.0199</span>
    </div>
  </div>
</body>
</html>
```